Have a New Tub or Shower in a Day!* Tub to New Tub or Tub to New Shower.

We need a postcard design for our Bath transformation product.
West Michigan Corvala dealer.
Lifetime Warranty on Corvala Wall System
Change a Tub or Shower to a New Tub or Shower in a Day!*
*Typically a day. (this could be on back of postcard?)
Free 24" Chrome Grab Bar
We remove the tub or shower and install a new tub or shower base.
Grab Bar Installation

Target Market(s)

seniors

Industry/Entity Type

Residential Construction

Requirements
Must have
• Description
• My images
• QRC logo with A+ on the right side of it
• Tidewell Home Improvement
• 4817 Marlow St.
• Fenmore, OR 97455
• (541) 555-0147
• www.tidewellhomeimprovement.example

```html
<!DOCTYPE html>
<html lang="en">
<head>
<meta charset="utf-8">
<title>Tidewell Home Improvement – Bath Postcard</title>
<link rel="stylesheet" href="https://fonts.googleapis.com/css2?family=Oswald:wght@400;500;600;700&family=Open+Sans:wght@400;600;700&display=swap">
<style>
  :root{
    --ink:#111111;
    --black:#0b0b0b;
    --green:#8dc63f;
    --white:#ffffff;
    --grey:#9a9a9a;
    --stage:#d9d9d6;
    --warm-1:#e9b983;
    --warm-2:#a6663a;
    --bath-1:#d9d6cf;
    --bath-2:#8f8a82;
  }
  *{margin:0;padding:0;box-sizing:border-box}
  html,body{width:900px;height:1200px;overflow:hidden;background:var(--stage)}
  .canvas{position:relative;width:900px;height:1200px}
  .postcard{position:absolute;left:40px;width:820px;height:565px;background:var(--white);overflow:hidden;box-shadow:0 4px 14px rgba(0,0,0,.25)}
  .postcard--front{top:30px}
  .postcard--back{top:620px}
  .postcard svg.shapes{position:absolute;inset:0;width:100%;height:100%}

  /* front */
  .badge{position:absolute;left:34px;top:30px;width:156px;height:52px;background:var(--ink)}
  .offer{position:absolute;left:40px;top:210px;width:220px;text-align:center;color:var(--white);font-family:"Oswald",sans-serif}
  .offer__small{font-size:15px;font-weight:500;letter-spacing:1px}
  .offer__amount{display:inline-block;margin-top:4px;background:var(--white);color:var(--ink);font-size:22px;font-weight:700;padding:0 8px;line-height:1.25}
  .offer__free{font-size:58px;font-weight:700;line-height:1;margin-top:2px}
  .headline{position:absolute;left:34px;top:402px;color:var(--white);font-family:"Oswald",sans-serif;font-weight:700;text-transform:uppercase;line-height:1.02}
  .headline__main{font-size:48px;display:block}
  .headline__sub{font-size:36px;display:block}
  .front-web{position:absolute;right:30px;top:452px;color:var(--white);font:600 17px "Open Sans",sans-serif}

  /* back */
  .message{position:absolute;left:32px;top:178px;width:340px;color:var(--white)}
  .message__kicker{font:700 24px/1 "Oswald",sans-serif;color:var(--green);text-transform:uppercase}
  .message__title{font:600 19px/1.15 "Oswald",sans-serif;text-transform:uppercase;margin-top:4px}
  .message__body{font:400 10.5px/1.45 "Open Sans",sans-serif;margin-top:12px;color:#e6e6e6}
  .contact{position:absolute;left:32px;top:432px;color:var(--white);font:400 11px/1.5 "Open Sans",sans-serif}
  .contact__title{font:700 22px/1 "Oswald",sans-serif;color:var(--green);text-transform:uppercase;margin-bottom:6px}
  .stamp-box{position:absolute;right:48px;top:40px;width:84px;height:100px;border:2px solid #555}
  .address-lines{position:absolute;left:470px;top:290px;width:300px}
  .address-lines span{display:block;height:1px;background:#555;margin-bottom:44px}
</style>
</head>
<body>
<div class="canvas">

  <section class="postcard postcard--front">
    <svg class="shapes" viewBox="0 0 820 565">
      <defs>
        <linearGradient id="warmShower" x1="0" y1="0" x2="1" y2="1">
          <stop offset="0" stop-color="#e9b983"/>
          <stop offset="1" stop-color="#a6663a"/>
        </linearGradient>
        <linearGradient id="bathRoom" x1="0" y1="0" x2="1" y2="1">
          <stop offset="0" stop-color="#d9d6cf"/>
          <stop offset="1" stop-color="#8f8a82"/>
        </linearGradient>
        <clipPath id="offerCircle"><circle cx="150" cy="230" r="118"/></clipPath>
      </defs>
      <path role="img" aria-label="Photo of a person rinsing off under a handheld shower in a candle-lit bathroom"
            d="M400 0 H820 V250 C660 310 500 290 430 200 C400 150 395 60 400 0Z" fill="url(#warmShower)"/>
      <path d="M0 292 C260 262 520 342 820 226 L820 282 C500 382 250 302 0 332Z" fill="#8dc63f"/>
      <path d="M0 332 C250 302 500 382 820 282 L820 565 L0 565Z" fill="#0b0b0b"/>
      <g clip-path="url(#offerCircle)">
        <rect role="img" aria-label="Photo of a remodeled bathroom with a new walk-in shower" x="30" y="110" width="240" height="100" fill="url(#bathRoom)"/>
        <rect x="30" y="200" width="240" height="150" fill="#0b0b0b"/>
      </g>
      <circle cx="150" cy="230" r="118" fill="none" stroke="#ffffff" stroke-width="6"/>
    </svg>

    <div class="badge" role="img" aria-label="Accreditation badge"></div>

    <div class="offer">
      <div class="offer__small">CHROME GRAB BAR</div>
      <div class="offer__amount">UP TO 24"</div>
      <div class="offer__free">FREE</div>
    </div>

    <h1 class="headline">
      <span class="headline__main">Have a new tub</span>
      <span class="headline__sub">or shower in a day!</span>
    </h1>
    <div class="front-web">www.tidewellhomeimprovement.example</div>
  </section>

  <section class="postcard postcard--back">
    <svg class="shapes" viewBox="0 0 820 565">
      <defs>
        <linearGradient id="bathRoomBack" x1="0" y1="0" x2="1" y2="1">
          <stop offset="0" stop-color="#d9d6cf"/>
          <stop offset="1" stop-color="#8f8a82"/>
        </linearGradient>
      </defs>
      <path d="M0 0 H410 V565 H0Z" fill="#0b0b0b"/>
      <path role="img" aria-label="Photo of a bright bathroom with a tiled shower and window"
            d="M70 0 H410 V160 H110 C90 110 78 60 70 0Z" fill="url(#bathRoomBack)"/>
      <path d="M0 0 H52 C60 70 78 125 105 165 L0 165Z" fill="#ffffff"/>
      <path d="M52 0 C60 70 78 125 105 165 L88 165 C62 125 44 70 38 0Z" fill="#8dc63f"/>
    </svg>

    <div class="message">
      <div class="message__kicker">Let us remodel</div>
      <div class="message__title">Your bathroom by personalizing it!</div>
      <p class="message__body">If it is time to give your bathroom a fresh new look and also update to some of today's amenities, Tidewell Home Improvement can help. From new tub or shower to a total bathroom remodel, Dale wants you to know he is here to help. He offers a no obligation in home consultation that will help you pick the right design, materials and colors to make your bathroom remodeling project an escape from the everyday hustle and bustle of work, kids and commitments that often find you tired and drained by the end of the day.</p>
    </div>

    <div class="contact">
      <div class="contact__title">Contact</div>
      Tidewell Home Improvement<br>
      4817 Marlow St.<br>
      Fenmore, OR 97455<br>
      (541) 555-0147<br>
      www.tidewellhomeimprovement.example
    </div>

    <div class="stamp-box"></div>
    <div class="address-lines"><span></span><span></span><span></span><span></span></div>
  </section>

</div>
</body>
</html>
```